Web Page Graphics

I require graphics work on shopping cart websites- banners, callouts, etc..
It is for a store that sells security cameras. I'd like to approach with a minimalist design; simple, uncluttered..
To start, I need a simple 200 x 266 callout graphic for an online store that tells users technical support is available, provides a phone number and hours. Simple.
Next, I need 3 main banners @ 770 x 328 each, illustrating various products, categories, and text in the form of features (or bullet points)
Lastly, 4 smaller callouts will appear under main banner @ 191 x 75 each. These will each include a vector icon and provide basic info, Ex: lowest prices, free shipping, etc. Text should just be placeholder dummy text.
Updates
Please see attached files.
Please note- project is for 3 banners, callout, and 4 small text boxes (see mockup)
Target Market(s)
Retail - small business and home owners
Industry/Entity Type
Shopping
Requirements
Must have
- Prior work to show

```html
<!DOCTYPE html>
<html lang="en">
<head>
<meta charset="utf-8">
<title>Vantage Security Store</title>
<link rel="stylesheet" href="https://fonts.googleapis.com/css2?family=Open+Sans:wght@400;600;700&family=Roboto+Condensed:ital,wght@0,400;0,700;1,400;1,700&display=swap">
<style>
:root{
  --red:#e8604c;
  --red-dark:#d2402d;
  --text:#3a3a3a;
  --muted:#777;
  --line:#dcdcdc;
  --panel:#f4f4f4;
  --lime:#b8d433;
  --yellow:#ffe14a;
  --notice:#fdfbe6;
  --notice-line:#e9dc8c;
  --ink:#1e1e1e;
  --orange:#f5820f;
}
*{box-sizing:border-box;margin:0;padding:0}
html,body{width:1200px;height:1152px;overflow:hidden;background:#fff}
body{font-family:"Open Sans",Arial,sans-serif;color:var(--text)}
.page{position:absolute;left:0;top:0;width:1044px;height:1009px;transform:scale(1.1494,1.1417);transform-origin:0 0;overflow:hidden}
.abs{position:absolute}

.topbar{left:0;top:0;width:1044px;height:31px;background:linear-gradient(#fafafa,#e6e6e6);border-bottom:1px solid #d4d4d4;font-size:11.5px}
.topbar .links{position:absolute;right:123px;top:7px;display:flex;gap:6px;color:#555}
.topbar .welcome{color:var(--red)}
.topbar .sep{color:#bbb}

.logo{left:115px;top:58px;display:flex;align-items:center;gap:8px}
.logo .mark{width:34px;height:34px;background:var(--red)}
.logo .name{font-size:24px;font-weight:400;color:#888}

.perk{top:60px;display:flex;gap:8px;font-size:10.5px;line-height:12.5px;color:#888}
.perk svg{flex:none;margin-top:4px}
.perk-div{top:60px;width:1px;height:40px;background:var(--line)}

.hotline{left:665px;top:48px;font-size:13.5px;font-weight:700;color:#333;display:flex;align-items:center;gap:6px}
.minicart{left:808px;top:48px;font-size:11.5px;color:#777;display:flex;align-items:center;gap:6px}
.search{left:665px;top:81px;width:268px;height:38px;background:var(--lime);border-radius:3px;padding:7px 6px 0 8px;display:flex;gap:6px}
.search .field{width:192px;height:24px;background:#fff;border:1px solid #ddd;border-radius:2px;font-size:11.5px;padding:4px 5px;color:#444}
.search .btn{width:56px;height:24px;background:var(--red);color:#fff;border-radius:3px;font-size:11.5px;font-weight:700;text-align:center;line-height:24px}

.sidebox{left:115px;width:169px;background:var(--panel);border:1px solid #e2e2e2;border-radius:3px;font-size:11.5px}
.sidebox h3{font-weight:400;font-size:13px;color:var(--red);padding:8px 7px 6px;border-bottom:3px double #ccc}
.sidebox p{padding:9px 7px;line-height:15px;color:#555}

.categories{left:115px;top:118px;width:169px;height:216px;background:#e9e9e9;border:1px solid #d0d0d0;border-radius:3px;padding:5px 6px}
.categories .head{height:27px;background:var(--red);border-radius:3px;color:#fff;font-size:13px;padding:5px 8px;position:relative}
.categories .head .toggle{position:absolute;right:5px;top:5px;width:17px;height:17px;border-radius:50%;background:#fff}
.categories ul{list-style:none;background:#fff;margin-top:2px}
.categories li{height:25.5px;border-bottom:1px solid #ddd;font-size:11px;color:#555;padding:5px 7px;position:relative;white-space:nowrap}
.categories li.more::after{content:"";position:absolute;right:8px;top:9px;width:5px;height:5px;border-right:1.5px solid #999;border-top:1.5px solid #999;transform:rotate(45deg)}

.support{left:115px;top:540px;width:169px;height:225px;background:linear-gradient(160deg,#c81a1a,#8f0c0c 60%,#b11616);color:#fff;font-family:"Roboto Condensed",Arial,sans-serif;font-style:italic;text-align:center}
.support .t1{position:absolute;top:28px;width:100%;font-size:31px;font-weight:700;color:var(--yellow)}
.support .t2{position:absolute;top:60px;width:100%;font-size:22px}
.support .t3{position:absolute;top:82px;width:100%;font-size:28px;font-weight:700}
.support .call{position:absolute;top:136px;width:100%;font-size:17px}
.support .num{position:absolute;top:158px;width:100%;height:26px;background:var(--red);font-size:21px;font-weight:700;line-height:26px}
.support .hrs{position:absolute;top:190px;width:100%;font-size:15px;font-weight:700;color:var(--yellow)}

.poll .q{padding:11px 10px 4px;color:#555}
.poll .opt{display:flex;align-items:center;gap:5px;padding:3px 10px;color:#555}
.poll .opt i{width:11px;height:11px;border:1px solid #999;border-radius:50%;background:#fff}
.poll .vote{position:absolute;right:14px;bottom:9px;padding:3px 9px;background:linear-gradient(#f7f7f7,#dcdcdc);border:1px solid #ccc;border-radius:2px;font-size:11.5px;color:#333}

.nav{left:283px;top:119px;width:650px;height:39px;background:linear-gradient(#f6f6f6,#e3e3e3);border-bottom:1px solid #d0d0d0;display:flex;font-size:12.5px}
.nav a{padding:11px 14px;border-right:1px solid #ccc;color:#333;text-decoration:none}
.nav a.active{color:var(--red)}

.hero{left:291px;top:167px;width:642px;height:273px;background:#fff;overflow:hidden;font-family:"Roboto Condensed",Arial,sans-serif;font-style:italic}
.hero .backdrop{position:absolute;left:0;top:0;width:642px;height:259px;background:linear-gradient(170deg,#ffffff 30%,#f6e3d3 60%,#f3d2b5 100%)}
.hero .headline{position:absolute;left:24px;top:31px;font-size:32px;font-weight:700;color:var(--red-dark);letter-spacing:.3px}
.hero .sub{position:absolute;left:22px;top:63px;font-size:22px;line-height:19px;color:#333}
.hero .foot{position:absolute;left:14px;top:226px;font-size:14px;color:#222}
.hero .phones{position:absolute;left:272px;top:118px;width:356px;height:130px;background:linear-gradient(#4a5560,#1f262c);border-radius:6px}
.hero .app{position:absolute;top:36px;width:44px;height:44px;border-radius:9px}
.hero .stripe{position:absolute;left:0;bottom:0;width:642px;height:14px;background:linear-gradient(100deg,var(--red) 65%,#aaa 65%)}

.callout{top:449px;width:159px;height:62px;border:1px solid #ddd;text-align:center;font-family:Arial,sans-serif;font-size:15px;padding-top:34px;letter-spacing:.2px;white-space:nowrap}
.callout.red{background:linear-gradient(#ef6a55,#d64a34);color:#fff}
.callout.light{background:linear-gradient(#fff,#ececec);color:var(--red)}
.callout svg{position:absolute;left:50%;top:5px;transform:translateX(-50%)}

.section{left:291px;width:643px;background:var(--panel);border:1px solid #e2e2e2;border-radius:3px}
.section h2{font-weight:400;font-size:13px;color:var(--red);padding:10px 12px}
.notice{margin:0 9px;height:34px;background:var(--notice);border:1px solid var(--notice-line);font-size:11.5px;color:#444;padding:8px 12px;display:flex;gap:6px;align-items:center}
.notice i{width:10px;height:10px;border-radius:50%;background:#f0c23a}

.promo{top:609px;width:207px;height:85px;border:1px solid #ddd;border-radius:3px;background:#fff}
.promo .pic{position:absolute;left:10px;top:6px;width:58px;height:72px;border-radius:4px}
.promo .label{position:absolute;right:10px;top:24px;width:118px;border-bottom:2px solid #f0a092;font-family:"Roboto Condensed",Arial,sans-serif;font-size:16px;color:#333;text-align:right;padding-bottom:2px}
.promo .cta{position:absolute;right:18px;top:48px;font-size:11.5px;color:var(--red)}
</style>
</head>
<body>
<div class="page">

  <div class="abs topbar">
    <div class="links"><span class="welcome">Default welcome msg!</span><span>My Account</span><span class="sep">|</span><span>My Wishlist</span><span class="sep">|</span><span>Checkout</span><span class="sep">|</span><span>Log In</span></div>
  </div>

  <div class="abs logo"><span class="mark"></span><span class="name">Vantage</span></div>

  <div class="abs perk" style="left:285px">
    <svg width="28" height="18" viewBox="0 0 28 18"><rect x="1" y="2" width="16" height="11" fill="#aaa"/><path d="M17 6h6l4 4v3H17z" fill="#aaa"/><circle cx="6" cy="15" r="2.5" fill="#888"/><circle cx="22" cy="15" r="2.5" fill="#888"/></svg>
    <span>Free Shipping<br>On All<br>Products</span>
  </div>
  <div class="abs perk-div" style="left:401px"></div>
  <div class="abs perk" style="left:411px">
    <svg width="30" height="16" viewBox="0 0 30 16"><rect x="1" y="2" width="28" height="12" fill="#aaa"/><rect x="7" y="4" width="3" height="8" fill="#ddd"/><rect x="20" y="4" width="3" height="8" fill="#ddd"/></svg>
    <span>Money Back<br>Guarantee</span>
  </div>
  <div class="abs perk-div" style="left:528px"></div>
  <div class="abs perk" style="left:539px">
    <svg width="18" height="20" viewBox="0 0 18 20"><rect x="1" y="7" width="16" height="12" fill="#aaa"/><rect x="0" y="4" width="18" height="4" fill="#999"/><rect x="8" y="4" width="2" height="15" fill="#ddd"/></svg>
    <span>Special weekly<br>Offer</span>
  </div>

  <div class="abs hotline">
    <svg width="13" height="11" viewBox="0 0 13 11"><path d="M1 3c0-2 11-2 11 0v2H9V3H4v2H1z" fill="#444"/><rect x="2" y="6" width="9" height="5" rx="1" fill="#444"/></svg>
    000 000 000
  </div>
  <div class="abs minicart">
    <svg width="24" height="18" viewBox="0 0 24 18"><path d="M1 2h4l3 10h12l3-8H7" fill="none" stroke="#6ab02b" stroke-width="2"/><circle cx="9" cy="15.5" r="2" fill="#6ab02b"/><circle cx="18" cy="15.5" r="2" fill="#6ab02b"/></svg>
    (0 item) - $0.00
    <svg width="10" height="6" viewBox="0 0 10 6"><path d="M0 0h10L5 6z" fill="#999"/></svg>
  </div>
  <div class="abs search"><div class="field">Search entire store here...</div><div class="btn">Search</div></div>

  <div class="abs categories">
    <div class="head">Categories<span class="toggle"></span></div>
    <ul>
      <li class="more">Analog Cameras</li>
      <li class="more">Digital Video Recorders</li>
      <li class="more">IP Cameras</li>
      <li class="more">Network Video Recorders</li>
      <li class="more">Accessories</li>
      <li>Network</li>
      <li style="border-bottom:0">Storage</li>
    </ul>
  </div>

  <div class="abs sidebox" style="top:345px;height:88px"><h3>My Cart</h3><p>You have no items in your shopping cart.</p></div>
  <div class="abs sidebox" style="top:444px;height:86px"><h3>Compare Products</h3><p>You have no items to compare.</p></div>

  <div class="abs support">
    <div class="t1">TECHNICAL</div>
    <div class="t2">support is</div>
    <div class="t3">Available</div>
    <div class="call">Call us Now</div>
    <div class="num">111-222-3333</div>
    <div class="hrs">24 hours available</div>
  </div>

  <div class="abs sidebox poll" style="top:775px;height:182px">
    <h3>Community Poll</h3>
    <div class="q">What is your favorite color</div>
    <div class="opt"><i></i>Green</div>
    <div class="opt"><i></i>Red</div>
    <div class="opt"><i></i>Black</div>
    <div class="opt"><i></i>Magenta</div>
    <div class="vote">Vote</div>
  </div>

  <div class="abs sidebox" style="top:968px;height:60px"><h3>Shop By Brand</h3></div>

  <nav class="abs nav">
    <a class="active">Home</a><a>About Us</a><a>Privacy Policy</a><a>Customer Service</a>
  </nav>

  <div class="abs hero">
    <div class="backdrop" role="img" aria-label="Sweeping orange and black decorative wave behind the banner"></div>
    <div class="headline">SMARTPHONE ACCESS</div>
    <div class="sub">View your cameras on any Phonix<br>Tablo or Droidal phone or tablet</div>
    <div class="app" style="left:347px;background:#2f8fd8"></div>
    <div class="app" style="left:405px;background:#4fb66a"></div>
    <div class="phones" role="img" aria-label="Row of five smartphones showing camera viewing app screens"></div>
    <div class="foot">CMS software for desktop Macra and Winsys</div>
    <div class="stripe"></div>
  </div>

  <div class="abs callout red" style="left:292px">
    <svg width="26" height="26" viewBox="0 0 26 26"><path d="M4 12L14 2h9v9L13 21z" fill="#fff"/><circle cx="19" cy="6" r="2" fill="var(--red)"/></svg>
    LOWEST PRICES</div>
  <div class="abs callout light" style="left:452px">
    <svg width="26" height="26" viewBox="0 0 26 26"><rect x="10" y="3" width="12" height="10" fill="#e8b83a"/><path d="M3 24L10 13" stroke="#333" stroke-width="2"/><circle cx="5" cy="23" r="2" fill="#333"/></svg>
    FREE SHIPPING</div>
  <div class="abs callout red" style="left:614px">
    <svg width="26" height="26" viewBox="0 0 26 26"><path d="M4 12L14 2h9v9L13 21z" fill="#fff"/><circle cx="19" cy="6" r="2" fill="var(--red)"/></svg>
    LOWEST PRICES</div>
  <div class="abs callout light" style="left:774px">
    <svg width="26" height="26" viewBox="0 0 26 26"><rect x="10" y="3" width="12" height="10" fill="#e8b83a"/><path d="M3 24L10 13" stroke="#333" stroke-width="2"/><circle cx="5" cy="23" r="2" fill="#333"/></svg>
    FREE SHIPPING</div>

  <section class="abs section" style="top:518px;height:80px">
    <h2>Latest Products</h2>
    <div class="notice"><i></i>There are no products matching the selection.</div>
  </section>

  <div class="abs promo" style="left:291px">
    <div class="pic" role="img" aria-label="Network video recorder unit" style="background:linear-gradient(#555,#1c1c1c)"></div>
    <div class="label">Network Video</div><div class="cta">See More</div>
  </div>
  <div class="abs promo" style="left:509px">
    <div class="pic" role="img" aria-label="Pan tilt zoom dome camera" style="background:linear-gradient(#f2f2f2,#b9b9b9)"></div>
    <div class="label">Pan/Tilt/Zoom</div><div class="cta">Shop Now</div>
  </div>
  <div class="abs promo" style="left:727px">
    <div class="pic" role="img" aria-label="HD dome security camera" style="left:6px;width:78px;background:linear-gradient(#fafafa,#bdbdbd)"></div>
    <div class="label">1080P HD Video</div><div class="cta">View All</div>
  </div>

  <section class="abs section" style="top:706px;height:80px">
    <h2>Featured Products</h2>
    <div class="notice"><i></i>There are no products matching the selection.</div>
  </section>

</div>
</body>
</html>
```